Exclusive beauty salon needs a price list or services booklet

I need a new very attractive flyer for my beauty salon, containing information on the different services and their prices.
In attachment you can find a pdf of the "old" one, but I'd love to have a beautifully designed new one!
I'd love to have a booklet in format 148 x 148 mm, or in US format, containing 12 or 16 pages, but if you can offer other nice looking designs they are welcome!
The services that need to come in the booklet with their prices can all be found on my website: www.atelierkova.be, starting with
Gelaatsverzorging
Wimperverlenging
Suikerontharing
Wimperlifting
Permanente Make Up
Airbrush Tanning

Target Market(s)

woman from 20 to 89 years old

Industry/Entity Type

Beauty Salon

Font styles to use
Sans Serif

Colors

Designer to choose colors to be used in the design.

Requirements
Must have
• a classy nice look, it must contain details about the services from my beauty salon and their prices, and nice pictures.
• The Names, prices and explanations of the services can easily be found on my website: www.atelierkova.be
Nice to have
• In attachment you can find the "old" price list in pdf, what I need now is a "new booklet" with the new logo and updated services price list.
• I need a very nice and attractive looking booklet, classy chique, Paris chique, looking very expensive.
Should not have
• Not too much colors, not too curly, but still feminine

```html
<!DOCTYPE html>
<html lang="nl">
<head>
<meta charset="utf-8">
<title>Ontharing met suiker – Tarieven</title>
<link href="https://fonts.googleapis.com/css2?family=Jost:wght@500&family=Caladea&display=swap" rel="stylesheet">
<style>
  :root {
    --teal: #8dcdc5;
    --pink: #e9b9c0;
    --ink: #111111;
    --honey: #e9a53a;
    --skin: #ecd2c0;
    --white: #ffffff;
  }
  * { margin: 0; padding: 0; box-sizing: border-box; }
  html, body { width: 1200px; height: 600px; overflow: hidden; background: var(--white); }
  .spread { display: flex; width: 1200px; height: 600px; color: var(--ink); font-family: "Caladea", serif; }

  .info-page { width: 600px; height: 600px; background: var(--teal); display: flex; flex-direction: column; }
  .info-body { height: 412px; padding: 26px 18px 0 24px; overflow: hidden; }
  .page-title {
    font-family: "Jost", sans-serif; font-weight: 500; font-size: 19px; line-height: 24px;
    letter-spacing: 0.5px; text-align: center;
  }
  .intro { font-size: 16.6px; line-height: 22px; text-align: center; margin: 11px 0 4px; padding: 0 8px; }
  .benefits-lead, .benefits { font-size: 13.4px; line-height: 16.5px; }
  .benefits { list-style: none; }
  .benefits li { position: relative; padding-left: 16px; }
  .benefits li::before { content: "•"; position: absolute; left: 1px; top: 0; font-size: 15px; }

  .photo-strip { display: flex; height: 188px; }
  .photo { width: 150px; height: 188px; }
  .photo-sugar { background: linear-gradient(160deg, #f3d6c6 0%, var(--honey) 55%, #f7eee6 100%); }
  .photo-underarm { background: linear-gradient(180deg, #f6e6dc 0%, var(--skin) 60%, #f4e7de 100%); }
  .photo-back { background: linear-gradient(180deg, #f4f1ee 0%, #d9b29a 45%, #c99c82 100%); }
  .photo-legs { background: linear-gradient(200deg, #ffffff 0%, #f1dccf 60%, #ffffff 100%); }

  .price-page { width: 600px; height: 600px; background: var(--pink); padding: 26px 40px 0 37px; }
  .price-title { font-family: "Jost", sans-serif; font-weight: 500; font-size: 19px; line-height: 24px; letter-spacing: 0.5px; text-align: center; margin-bottom: 17px; }
  .price-list { list-style: none; font-size: 17px; }
  .price-row { display: flex; align-items: baseline; height: 41.7px; padding-top: 11px; }
  .price-name { white-space: nowrap; }
  .price-leader { flex: 1; border-bottom: 1.5px dotted var(--ink); margin: 0 10px 0 1px; transform: translateY(-3px); }
  .price-amount { white-space: nowrap; width: 33px; text-align: right; }
</style>
</head>
<body>
<main class="spread">
  <section class="info-page">
    <div class="info-body">
      <h1 class="page-title">ONTHARING MET SUIKER</h1>
      <p class="intro">Heb je ook genoeg van lichaams- en/of gezichtsbeharing maar ben je niet tevreden met het resultaat van scheren/harsen/laseren? Dan is ontharen met suiker van Kova's dé oplossing!</p>
      <p class="benefits-lead">De voordelen van ontharen met suiker:</p>
      <ul class="benefits">
        <li>De haren worden met de haargroeirichting verwijderd, hierdoor verminderd de pijn en je hebt geen last van haartjes die afbreken</li>
        <li>De haren worden volledig verwijderd (met de haarwortel) waardoor ze dunner en donziger worden en minder snel aangroeien</li>
        <li>Er wordt hygiënisch gewerkt</li>
        <li>De huidstructuur verbetert door het verwijderen van dode huidcellen zonder de levende cellen te beschadigen</li>
        <li>Suiker bestaat uit lichaamseigen stoffen waardoor de huid minder fel reageert op de ontharing.</li>
        <li>Suikerontharing zorgt ervoor dat de haargroei vermindert na iedere behandeling en verfijnt de haarstructuur</li>
        <li>met suikerontharing werkt men op lichaamstemperatuur dus geen brandwonden</li>
        <li>suikerontharing is geschikt voor de couperose huid en is uiterst geschikt voor de meest gevoelige plaatsen (bikini, gezicht,...)</li>
        <li>suiker is wateroplosbaar, dus geen ongewenste plakseltjes</li>
      </ul>
    </div>
    <div class="photo-strip">
      <div class="photo photo-sugar" role="img" aria-label="Foto: suikerpasta wordt op de huid aangebracht"></div>
      <div class="photo photo-underarm" role="img" aria-label="Foto: gladde oksel van een vrouw"></div>
      <div class="photo photo-back" role="img" aria-label="Foto: blote rug van een vrouw"></div>
      <div class="photo photo-legs" role="img" aria-label="Foto: gladde benen van een vrouw"></div>
    </div>
  </section>

  <section class="price-page">
    <h2 class="price-title">TARIEVEN</h2>
    <ul class="price-list">
      <li class="price-row"><span class="price-name">Wenkbrauwen</span><span class="price-leader"></span><span class="price-amount">€09</span></li>
      <li class="price-row"><span class="price-name">Wenkbrauwen En Bovenlip</span><span class="price-leader"></span><span class="price-amount">€16</span></li>
      <li class="price-row"><span class="price-name">Bovenlip Of Kin</span><span class="price-leader"></span><span class="price-amount">€09</span></li>
      <li class="price-row"><span class="price-name">Bovenlip En Kin</span><span class="price-leader"></span><span class="price-amount">€16</span></li>
      <li class="price-row"><span class="price-name">Gezicht (Bovenlip, Kin, Wangen en wenkbrauw)</span><span class="price-leader"></span><span class="price-amount">€25</span></li>
      <li class="price-row"><span class="price-name">Oksels</span><span class="price-leader"></span><span class="price-amount">€12</span></li>
      <li class="price-row"><span class="price-name">Armen</span><span class="price-leader"></span><span class="price-amount">€20</span></li>
      <li class="price-row"><span class="price-name">Brazilian Bikini Of String</span><span class="price-leader"></span><span class="price-amount">€30</span></li>
      <li class="price-row"><span class="price-name">Bikinilijn</span><span class="price-leader"></span><span class="price-amount">€15</span></li>
      <li class="price-row"><span class="price-name">Onderbeen En Knie</span><span class="price-leader"></span><span class="price-amount">€30</span></li>
      <li class="price-row"><span class="price-name">Bovenbenen</span><span class="price-leader"></span><span class="price-amount">€20</span></li>
      <li class="price-row"><span class="price-name">Volledige Benen (Zonder Bikini)</span><span class="price-leader"></span><span class="price-amount">€50</span></li>
    </ul>
  </section>
</main>
</body>
</html>
```